Cafe Business needs a business card design

I already have an ai logo I would like to use and color. I need someone to make a business card for me on adobe illustrator with it. Its for a cafe restaurant opening in Japan I would like to be able to change out the names, contact info, ect on my own from adobe illustrator.

Industry/Entity Type

Business

Contact Information for Business Card

Double sided with logo on one side and info on the other. Name, Tel, fax, email and west

```html
<!DOCTYPE html>
<html lang="en">
<head>
<meta charset="UTF-8">
<title>Kumo Bean Cafe – Business Card</title>
<link href="https://fonts.googleapis.com/css2?family=Patrick+Hand+SC&display=swap" rel="stylesheet">
<style>
  :root {
    --orange: #fb9a3a;
    --white: #ffffff;
    --ink: #1c1c1c;
    --brown: #5a2d14;
    --beige: #efe3c8;
    --shadow: #555555;
    --bg: #ffffff;
  }
  * { margin: 0; padding: 0; box-sizing: border-box; }
  html, body { width: 1200px; height: 1200px; overflow: hidden; background: var(--bg); }
  body { position: relative; font-family: "Patrick Hand SC", cursive; color: var(--ink); }

  .card { position: absolute; box-shadow: 19px 19px 14px var(--shadow); }

  /* Front side */
  .card-front { left: 298px; top: 173px; width: 609px; height: 350px; background: var(--orange); }
  .brand-header { position: absolute; left: 298px; top: 26px; display: flex; align-items: center; gap: 12px; }
  .brand-dot { width: 62px; height: 62px; border-radius: 50%; background: var(--white); }
  .brand-name { font-size: 30px; color: var(--white); }

  .info-panel { position: absolute; left: 12px; top: 141px; width: 578px; height: 192px; background: var(--white); }
  .cup-art { position: absolute; left: 50px; top: 34px; width: 110px; height: 120px; border-radius: 8px;
             background: linear-gradient(180deg, #b88a62 0%, var(--brown) 100%); }
  .divider { position: absolute; left: 189px; top: 27px; width: 3px; height: 151px; background: var(--ink); }

  .contact-list { position: absolute; left: 238px; top: 22px; list-style: none; }
  .contact-list li { display: flex; align-items: center; gap: 10px; height: 42px; font-size: 16px; letter-spacing: 0.5px; }
  .contact-icon { width: 28px; height: 28px; flex: none; }

  /* Back side */
  .card-back { left: 298px; top: 595px; width: 614px; height: 348px; background: var(--white); }
  .side-tab { position: absolute; left: 0; top: 65px; width: 57px; height: 240px; }
  .back-brand { position: absolute; left: 225px; top: 89px; width: 154px; height: 175px;
                display: flex; align-items: center; justify-content: center; gap: 8px; }
  .back-brand-mark { width: 18px; height: 18px; background: var(--brown); flex: none; }
  .back-brand-name { font-size: 26px; color: var(--brown); white-space: nowrap; }
</style>
</head>
<body>

  <section class="card card-front">
    <div class="brand-header">
      <span class="brand-dot"></span>
      <span class="brand-name">Kumo Bean Cafe</span>
    </div>

    <div class="info-panel">
      <div class="cup-art" role="img" aria-label="Illustration of a steaming coffee cup on a saucer"></div>
      <div class="divider"></div>

      <ul class="contact-list">
        <li>
          <svg class="contact-icon" viewBox="0 0 28 28"><circle cx="14" cy="14" r="13" fill="#1c1c1c"/><path d="M9 8c1-1 2-1 3 0l1 2c0 1-1 2-1 2 1 2 2 3 4 4 0 0 1-1 2-1l2 1c1 1 1 2 0 3-1 1-3 2-6 0-3-2-5-4-6-7-1-2 0-3 1-4z" fill="#fff"/></svg>
          <span>0000000000</span>
        </li>
        <li>
          <svg class="contact-icon" viewBox="0 0 28 28"><path d="M14 2a8 8 0 0 1 8 8c0 6-8 14-8 14S6 16 6 10a8 8 0 0 1 8-8z" fill="#1c1c1c"/><circle cx="14" cy="10" r="3" fill="#fff"/><ellipse cx="14" cy="25" rx="7" ry="2" fill="none" stroke="#1c1c1c" stroke-width="1.5"/></svg>
          <span>12 Sakura Lane, Nakamachi</span>
        </li>
        <li>
          <svg class="contact-icon" viewBox="0 0 28 28"><circle cx="14" cy="14" r="13" fill="#1c1c1c"/><g fill="none" stroke="#fff" stroke-width="1.5"><circle cx="14" cy="14" r="8"/><ellipse cx="14" cy="14" rx="3.5" ry="8"/><path d="M6 14h16M8 10h12M8 18h12"/></g></svg>
          <span>www.kumobean.com</span>
        </li>
        <li>
          <svg class="contact-icon" viewBox="0 0 28 28"><circle cx="14" cy="14" r="13" fill="#1c1c1c"/><rect x="7" y="9" width="14" height="10" rx="1" fill="#fff"/><path d="M7 9l7 6 7-6" fill="none" stroke="#1c1c1c" stroke-width="1.5"/></svg>
          <span>hello@kumobean.com</span>
        </li>
      </ul>
    </div>
  </section>

  <section class="card card-back">
    <svg class="side-tab" viewBox="0 0 57 240" preserveAspectRatio="none">
      <path d="M0 0 L52 10 Q57 120 52 230 L0 240 Z" fill="#fb9a3a"/>
    </svg>
    <div class="back-brand">
      <span class="back-brand-mark"></span>
      <span class="back-brand-name">KUMO BEAN</span>
    </div>
  </section>

</body>
</html>
```